Job Coaching - Vanta; engaging people to improve their work experience

I need a flyer for Job Coaching. It serves to engage customers (not businesses) with problems in their daily job, typical questions that are handled are:
Do I fit for the job?
Am I using my talents at best in this job?
I have a conflict with my manager/colleagues, what should I do?
My work-life balance is a mess, how can I improve this?
What job fits best with my talents?
I'm getting stressed out from my job, what can I do?
....
This Flyer will be available at GP's, therpeutic practices, pharamcists,...
this flyer should put people in action to contact me
Flyer can be created in English, in the final one the text should be in Dutch; I will make the translation of the selected flyer and provide it at the end

Target Market(s)

consumers / customers / people having a job, but somewhat stuck in it

Industry/Entity Type

Professional Coaching

Requirements
Must have
• the questions mentioned in the project description; mobile number: 0471/389145; email: tom.vermeer@vantacoaching.example; website: www.vantacoaching.example ; it should make also reference to 'Career guidance cheques of the KWOL'

```html
<!DOCTYPE html>
<html lang="en">
<head>
<meta charset="utf-8">
<title>Vanta Professional Coaching – Flyer</title>
<link rel="stylesheet" href="https://fonts.googleapis.com/css2?family=Bebas+Neue&family=Montserrat:wght@400;500;600;700&display=swap">
<style>
  :root{
    --teal:#3aa99c;
    --teal-light:#7fd8cd;
    --teal-text:#2fa89a;
    --ink:#1a1a1a;
    --grey:#5a5a5a;
    --tab-grey:#e4e4e4;
    --stage:#c6c6c6;
    --paper:#ffffff;
    --photo-warm:#b99a7c;
    --photo-deep:#6e3a2e;
  }
  *{margin:0;padding:0;box-sizing:border-box}
  html,body{width:1200px;height:2245px;overflow:hidden}
  body{background:var(--stage);font-family:"Montserrat",sans-serif;color:var(--ink);position:relative}

  .flyer{
    position:absolute;left:40px;top:337px;
    width:976px;height:1369px;background:var(--paper);
    transform:scale(1.1475);transform-origin:top left;
    box-shadow:0 6px 18px rgba(0,0,0,.35);overflow:hidden;
  }
  .header-art{position:absolute;left:0;top:0;width:976px;height:700px}

  .brand{position:absolute;left:58px;top:100px;display:flex;align-items:center;gap:16px}
  .brand-dot{width:58px;height:58px;border-radius:50%;background:var(--grey)}
  .brand-name{font-family:"Montserrat",sans-serif;font-weight:600;font-size:62px;color:var(--teal);letter-spacing:2px;line-height:1}

  .coach-name{position:absolute;right:58px;top:100px;text-align:right;white-space:nowrap}
  .coach-name strong{display:block;font-weight:600;font-size:24px;line-height:1.05}
  .coach-name span{display:block;font-weight:500;font-size:17px;line-height:1.3}

  .headline{position:absolute;left:60px;top:296px;font-family:"Bebas Neue",sans-serif;font-size:52px;line-height:56px;color:var(--ink);letter-spacing:.2px}

  .intro{position:absolute;left:62px;top:708px}
  .intro h2{font-weight:600;font-size:24.5px;color:var(--teal-text);letter-spacing:.2px}
  .intro h3{font-weight:700;font-size:15.5px;color:var(--grey);margin-top:8px}

  .points{position:absolute;left:64px;top:806px;width:440px;display:flex;flex-direction:column;gap:26px}
  .point{position:relative;width:440px;min-height:52px}
  .point-icon{position:absolute;left:0;top:0;width:52px;height:52px;border-radius:6px;background:var(--teal)}
  .point-icon svg{width:52px;height:52px}
  .point h4{margin-left:91px;font-weight:600;font-size:19px;line-height:25px}
  .point p{margin-left:92px;margin-top:12px;font-size:12.5px;line-height:15.5px;text-align:justify;color:#222}

  .story{position:absolute;left:548px;top:806px;width:366px;font-size:12.5px;line-height:15.5px;color:#222}
  .story p{text-align:justify;margin-bottom:6px}
  .story .ask{color:var(--teal-text);font-weight:600;font-size:15px;line-height:18px;letter-spacing:1px;margin:12px 0 8px;text-align:left}
  .questions{list-style:none}
  .questions li{position:relative;padding-left:24px;font-weight:600;font-size:12.5px;line-height:16px;margin-bottom:6px}
  .questions li::before{content:"";position:absolute;left:0;top:4px;width:8px;height:8px;background:var(--teal)}
  .story .together{color:var(--teal-text);font-weight:600;font-size:15px;margin-top:12px}

  .footer{position:absolute;left:0;top:1249px;width:976px;height:120px;background:var(--teal)}
  .footer-dark{position:absolute;left:0;top:0}
  .contact{position:absolute;top:35px;display:flex;align-items:center;gap:14px;font-size:13px;line-height:17px;color:var(--ink);white-space:nowrap}
  .contact-icon{width:50px;height:50px;border-radius:7px;background:var(--ink);flex:none}
  .contact-icon svg{width:50px;height:50px}
  .contact.phone{left:56px}
  .contact.mail{left:236px}
  .cheques{position:absolute;left:690px;top:40px;font-weight:700;font-size:16.5px;line-height:20px;color:var(--teal-light);white-space:nowrap}
</style>
</head>
<body>
<main class="flyer">

  <svg class="header-art" viewBox="0 0 976 700">
    <defs>
      <linearGradient id="photoTone" x1="0" y1="0" x2="1" y2="1">
        <stop offset="0" stop-color="#d9c4a8"/>
        <stop offset=".45" stop-color="var(--photo-warm)"/>
        <stop offset=".75" stop-color="var(--photo-deep)"/>
        <stop offset="1" stop-color="#3a2a2a"/>
      </linearGradient>
    </defs>
    <g role="img" aria-label="Portrait photo of the professional coach standing indoors">
      <path d="M235,0 L976,0 L976,688 L600,688 Q545,688 515,630 L235,0 Z" fill="url(#photoTone)"/>
    </g>
    <path d="M700,0 L976,0 L976,486 Q820,450 745,300 Q690,170 700,0 Z" fill="var(--teal-light)" opacity=".82"/>
    <path d="M700,150 Q760,40 860,40 L976,40" fill="none" stroke="var(--grey)" stroke-width="2" opacity=".6"/>
    <path d="M0,68 L375,68 Q395,68 402,85 L420,180 Q423,195 405,195 L0,195 Z" fill="var(--tab-grey)"/>
    <path d="M0,245 L405,245 L535,615 L0,615 Z" fill="var(--teal)"/>
    <path d="M0,615 L535,615 L541,632 L0,632 Z" fill="var(--ink)"/>
  </svg>

  <div class="brand">
    <span class="brand-dot"></span>
    <span class="brand-name">VANTA</span>
  </div>

  <div class="coach-name">
    <strong>TOM VERMEER</strong>
    <span>Professional Coach</span>
  </div>

  <h1 class="headline">Are there<br>any specific<br>techniques used for<br>problem solving<br>through coaching?</h1>

  <header class="intro">
    <h2>YOU CAN SOLVE YOUR QUESTIONS THROUGH OUR COACHING</h2>
    <h3>CAREER GUIDANCE (WITH CAREER VOUCHERS)</h3>
  </header>

  <section class="points">
    <article class="point">
      <span class="point-icon">
        <svg viewBox="0 0 52 52" fill="none" stroke="#fff" stroke-width="1.8">
          <rect x="12" y="14" width="28" height="19" rx="1.5"/>
          <path d="M22,33 L21,38 M30,33 L31,38 M17,39 L35,39"/>
          <rect x="20" y="18" width="12" height="7"/>
        </svg>
      </span>
      <h4>We easily spend<br>8 hours a day...</h4>
      <p>on our professional pursuits, our job. If we assume that we sleep about 8 hours a day, that's 50% of our active time. We actually spend more time with our colleagues than with our partner and/or children.</p>
    </article>
    <article class="point">
      <span class="point-icon">
        <svg viewBox="0 0 52 52" fill="none" stroke="#fff" stroke-width="1.8">
          <path d="M26,13 a9,9 0 0 1 6,16 v4 h-12 v-4 a9,9 0 0 1 6,-16 Z"/>
          <path d="M21,37 h10 M23,40 h6 M26,6 v3 M14,12 l2,2 M38,12 l-2,2 M10,23 h3 M39,23 h3"/>
        </svg>
      </span>
      <h4>In addition...</h4>
      <p>if things are not going well during those 8 hours, it also impacts the other 8 waking hours. If we don't feel good about ourselves at work, our family members, friends and acquaintances feel it too.</p>
    </article>
    <article class="point">
      <span class="point-icon">
        <svg viewBox="0 0 52 52" fill="none" stroke="#fff" stroke-width="1.8">
          <circle cx="26" cy="26" r="6"/>
          <circle cx="26" cy="26" r="10"/>
          <path d="M26,11 v4 M26,37 v4 M11,26 h4 M37,26 h4 M15.4,15.4 l2.8,2.8 M33.8,33.8 l2.8,2.8 M15.4,36.6 l2.8,-2.8 M33.8,18.2 l2.8,-2.8"/>
        </svg>
      </span>
      <h4>So we'd better make<br>sure that...</h4>
      <p>we spend those 8 hours meaningfully and, at best, get energy from it too. That we can accomplish a piece of our personal accomplishments there.</p>
    </article>
  </section>

  <section class="story">
    <p>Unfortunately, not every career goes smoothly, and it is even very normal that there are ups and downs this, nowadays more than 40-year career. But we can strive to keep these downs as short as possible and the ups as long as possible.</p>
    <p>And that's where Career Counseling comes into play.</p>
    <p>During this career counseling, we take a close look at your personal situation.</p>
    <p class="ask">Do you recognize yourself in any of the following questions?</p>
    <ul class="questions">
      <li>Do I fit for the job?</li>
      <li>Am I using my talents at best in this job?</li>
      <li>I have a conflict with my manager/colleagues, what should I do?</li>
      <li>My work-life balance is a mess, how can I improve this?</li>
      <li>What job fits best with my talents?</li>
      <li>I'm getting stressed out from my job, what can I do?</li>
    </ul>
    <p class="together">Then we will work on this together.</p>
  </section>

  <footer class="footer">
    <svg class="footer-dark" width="976" height="120" viewBox="0 0 976 120" aria-hidden="true">
      <path d="M600,0 L976,0 L976,120 L650,120 Z" fill="var(--ink)"/>
    </svg>
    <div class="contact phone">
      <span class="contact-icon">
        <svg viewBox="0 0 50 50"><path d="M16,13 l5,0 l3,7 l-3,3 q3,6 9,9 l3,-3 l7,3 l0,5 q-1,3 -4,3 q-12,-1 -20,-10 q-5,-7 -4,-14 q1,-3 4,-3 Z" fill="var(--teal)"/></svg>
      </span>
      <span>0471/389145</span>
    </div>
    <div class="contact mail">
      <span class="contact-icon">
        <svg viewBox="0 0 50 50" fill="none" stroke="var(--teal)" stroke-width="2"><rect x="12" y="16" width="26" height="18"/><path d="M12,16 L25,27 L38,16 M12,34 L21,24 M38,34 L29,24"/></svg>
      </span>
      <span>tom.vermeer@vantacoaching.example<br>www.vantacoaching.example</span>
    </div>
    <p class="cheques">Career Guidance Cheques<br>Of The KWOL</p>
  </footer>

</main>
</body>
</html>
```